Campaign Website

I need a website for my judicial campaign. I would like a site that directs from this domain as well as a new domain with my married last name. I need separate pages on the site that address my diversion programs, and a page to allow people to donate with a link to my bank account and a link for people to submit requests to volunteer, get yard signs, etc.

```html
<!DOCTYPE html>
<html lang="en">
<head>
<meta charset="utf-8">
<title>Harmon Delia – Judicial Campaign</title>
<link rel="stylesheet" href="https://fonts.googleapis.com/css2?family=Playfair+Display:wght@400;700&family=Open+Sans:wght@400;600&family=Tinos&display=swap">
<style>
:root{
  --navy:#0e2a52;
  --ink:#1d1d1d;
  --muted:#666;
  --panel:#e9e9e9;
  --panel-soft:#ececec;
  --card:#ffffff;
  --footer:#262626;
  --footer-text:#8a8a8a;
  --footer-line:#4a4a4a;
  --white:#fff;
}
*{box-sizing:border-box;margin:0;padding:0}
html,body{width:1200px;height:2487px;overflow:hidden}
body{font-family:"Open Sans",sans-serif;color:var(--ink);background:var(--white);position:relative}
.abs{position:absolute}
.line{display:block;white-space:nowrap}
.btn{position:absolute;display:flex;align-items:center;justify-content:center;background:var(--navy);color:var(--white);border-radius:22px;font-family:"Tinos",serif;text-transform:uppercase;font-size:12px;text-decoration:none}
h2.section-title{position:absolute;left:0;width:1200px;text-align:center;font-family:"Playfair Display",serif;font-weight:700;font-size:34px;color:var(--navy)}

/* header */
.site-header{position:absolute;top:0;left:0;width:1200px;height:78px}
.brand{left:145px;top:16px;font-family:"Playfair Display",serif;font-weight:700;font-size:34px;color:var(--ink)}
.main-nav{position:absolute;right:146px;top:24px;display:flex;align-items:center;gap:28px;font-family:"Tinos",serif;font-size:12px;text-transform:uppercase;color:#555}
.main-nav .active{color:var(--navy)}
.main-nav .nav-donate{background:var(--navy);color:var(--white);border-radius:16px;padding:8px 16px;margin-left:-8px}

/* hero */
.hero{position:absolute;top:78px;left:0;width:1200px;height:536px;background:linear-gradient(90deg,#3c2a20 0%,#5a4030 40%,#4a3628 70%,#3a2a20 100%)}
.hero-photo{position:absolute;left:200px;top:0;width:540px;height:536px;background:radial-gradient(ellipse at 50% 55%,#d9c9b0 0%,#8a6a50 55%,rgba(80,60,45,0) 75%)}
.hero-title{right:146px;top:200px;text-align:right;font-family:"Playfair Display",serif;font-weight:700;font-size:34px;line-height:38px;color:var(--white)}
.hero-cta{position:absolute;left:927px;top:287px;width:127px;height:42px;border:2px solid var(--white);border-radius:22px;display:flex;align-items:center;justify-content:center;color:var(--white);font-family:"Tinos",serif;font-size:17px}
.hero-arrow{position:absolute;top:252px}

/* welcome */
.welcome-title{left:145px;top:700px;font-family:"Playfair Display",serif;font-weight:700;font-size:34px;color:var(--navy)}
.welcome-text{left:145px;top:753px;width:600px;font-size:11.5px;line-height:22.4px}
.portrait{position:absolute;left:759px;top:676px;width:296px;height:296px;border-radius:50%;background:radial-gradient(circle at 50% 40%,#6a5a50 0%,#3a3434 50%,#121212 85%)}

/* events */
.events{position:absolute;top:1036px;left:0;width:1200px;height:384px;background:var(--panel)}
.event-card{position:absolute;top:127px;height:121px;background:var(--card);padding:18px 20px}
.event-card.raised{box-shadow:0 2px 8px rgba(0,0,0,.25)}
.event-date{font-family:"Playfair Display",serif;font-size:14px;color:var(--ink);margin-bottom:8px}
.event-text{font-size:11px;line-height:19px;color:var(--muted)}

/* diversion */
.program-card{position:absolute;top:1557px;width:296px;height:336px;background:var(--panel-soft)}
.program-card.raised{background:var(--card);box-shadow:0 2px 8px rgba(0,0,0,.3)}
.program-image{width:296px;height:200px}
.program-body{padding:16px 16px}
.program-date{font-family:"Playfair Display",serif;font-size:13px;margin-bottom:6px}
.program-title{font-family:"Playfair Display",serif;font-size:19.5px;line-height:25px;color:var(--ink)}

/* donate */
.donate{position:absolute;top:2034px;left:0;width:1200px;height:240px;background:var(--panel-soft)}
.donate-text{position:absolute;left:0;top:96px;width:1200px;text-align:center;font-size:11.5px;line-height:19px}
.donate-text .line{display:block}

/* footer */
.site-footer{position:absolute;top:2274px;left:0;width:1200px;height:213px;background:var(--footer)}
.social{position:absolute;top:32px;display:flex;align-items:center;gap:10px}
.social-ring{width:40px;height:40px;border:1px solid var(--footer-text);border-radius:50%}
.social small{display:block;font-size:11px;color:var(--footer-text)}
.social strong{display:block;font-size:15px;font-weight:600;color:var(--footer-text);text-transform:uppercase;line-height:18px}
.footer-rule{position:absolute;left:145px;top:105px;width:911px;height:1px;background:var(--footer-line)}
.footer-nav{position:absolute;top:134px;width:1200px;text-align:center;font-size:12px;color:var(--footer-text);word-spacing:2px}
.copyright{position:absolute;top:163px;width:1200px;text-align:center;font-size:12px;color:var(--footer-text)}
</style>
</head>
<body>

<header class="site-header">
  <div class="abs brand">Harmon Delia</div>
  <nav class="main-nav">
    <span class="active">Home</span><span>Bio</span><span>Events and Programs</span><span>Voting Info</span><span>Contact</span><span class="nav-donate">Donate</span>
  </nav>
</header>

<section class="hero">
  <div class="hero-photo" role="img" aria-label="Photo of the candidate and her husband embracing in front of a wooden fence"></div>
  <svg class="hero-arrow" style="left:55px" width="22" height="32" viewBox="0 0 22 32"><path d="M17 3 L5 16 L17 29" fill="none" stroke="#fff" stroke-width="4"/></svg>
  <svg class="hero-arrow" style="left:1123px" width="22" height="32" viewBox="0 0 22 32"><path d="M5 3 L17 16 L5 29" fill="none" stroke="#fff" stroke-width="4"/></svg>
  <div class="abs hero-title">Phasellus nisl est<br>condimentum vitae</div>
  <a class="hero-cta">VOTE NOW</a>
</section>

<section class="welcome">
  <h1 class="abs welcome-title">Welcome to Harmon Delia</h1>
  <p class="abs welcome-text">
    <span class="line">Aenean sed quam non sapien faucibus consequat vitae sit amet orci. Praesent quis risus mi. In mollis nulla in</span>
    <span class="line">pulvinar dictum. Vivamus interdum sagittis felis, ut dapibus ligula feugiat ac. In dictum sapien eu tellus finibus</span>
    <span class="line">fermentum. Aenean faucibus lacus ut mollis commodo. Donec vestibulum odio sem, ac laoreet massa ullamcorp</span>
    <span class="line">er id. Donec molestie nisi et tellus hendrerit vehicula. Nunc eu ligula sed qutam pulvinar maximus in vitae eros.</span>
    <span class="line">Proin porta fermentum ipsum, vel porttitor turpis venenatis luctus. Vivamus volutpat eu sapien quis tempus.</span>
    <span class="line">Aenean feugiat viverra lorem ac sagittis. Donec sit amet lectus nec mi tempor.</span>
  </p>
  <a class="btn" style="left:145px;top:898px;width:103px;height:40px">Read More</a>
  <div class="portrait" role="img" aria-label="Portrait of the candidate in judicial robe before flags"></div>
</section>

<section class="events">
  <h2 class="section-title" style="top:70px">Events and Programs</h2>
  <article class="event-card raised" style="left:145px;width:447px">
    <div class="event-date">12 August, 2019</div>
    <p class="event-text">Vestibulum condimentum, risus ut posuere cursus, velit justo accumsan sem, lobortis aliquet metus dui eu libero. Pellentesque a imperdiet dolor, et auctor est placerat dapibus gravida.</p>
  </article>
  <article class="event-card" style="left:608px;width:448px">
    <div class="event-date">12 August, 2019</div>
    <p class="event-text">Vestibulum condimentum, risus ut posuere cursus, velit justo accumsan sem, lobortis aliquet metus dui eu libero. Pellentesque a imperdiet dolor, et auctor est placerat dapibus gravida.</p>
  </article>
  <a class="btn" style="left:492px;top:265px;width:215px;height:39px">View all events &amp; programs</a>
</section>

<h2 class="section-title" style="top:1494px">Diversion Programs</h2>
<article class="program-card raised" style="left:145px">
  <div class="program-image" role="img" aria-label="Photo of a stone courthouse facade" style="background:linear-gradient(180deg,#b9bec4,#8e9297)"></div>
  <div class="program-body"><div class="program-date">12 August, 2019</div><div class="program-title"><span class="line">Suspendisse elit ligula, iaculis</span><span class="line">dignissim justo eu, vestibulum</span><span class="line">venenatis.</span></div></div>
</article>
<article class="program-card" style="left:452px">
  <div class="program-image" role="img" aria-label="Photo of an empty wood-paneled courtroom" style="background:linear-gradient(180deg,#4a2a1e,#6b3a28)"></div>
  <div class="program-body"><div class="program-date">12 August, 2019</div><div class="program-title"><span class="line">Fusce porta arcu mi, aliquet</span><span class="line">dictum nulla interdum quis.</span><span class="line">Donec quis ex semper.</span></div></div>
</article>
<article class="program-card" style="left:760px">
  <div class="program-image" role="img" aria-label="Photo of shelves of law books" style="background:linear-gradient(90deg,#2e3e58,#8a6a40,#2e3e58)"></div>
  <div class="program-body"><div class="program-date">12 August, 2019</div><div class="program-title"><span class="line">Phasellus elementum lacinia</span><span class="line">quam pellentesque. Aliquam</span><span class="line">malesuada.</span></div></div>
</article>
<a class="btn" style="left:516px;top:1914px;width:168px;height:40px">View all programs</a>

<section class="donate">
  <h2 class="section-title" style="top:44px">Donate</h2>
  <p class="donate-text">
    <span class="line">Pellentesque accumsan ut metus sed elementum. Integer ac ante neque. Vestibulum a eleifend sapien, at consectetur risus. Nulla finibus lacinia dolor, semper dictum leo</span>
    <span class="line">eleifend non. Etiam non nulla non turpis pharetra tincidunt sed ut lorem. Etiam bibendum eros at velit consectetur commodo.</span>
  </p>
  <a class="btn" style="left:528px;top:140px;width:144px;height:44px;font-size:16px">Donate now</a>
</section>

<footer class="site-footer">
  <div class="social" style="left:145px"><span class="social-ring"></span><span><small>Find us on</small><strong>Friendspace</strong></span></div>
  <div class="social" style="left:407px"><span class="social-ring"></span><span><small>Contact us on</small><strong>Worklink</strong></span></div>
  <div class="social" style="left:669px"><span class="social-ring"></span><span><small>View us on</small><strong>Videohub</strong></span></div>
  <div class="social" style="left:925px"><span class="social-ring"></span><span><small>Follow us on</small><strong>Photofeed</strong></span></div>
  <div class="footer-rule"></div>
  <div class="footer-nav">Home &nbsp;|&nbsp; Bio &nbsp;|&nbsp; Events and Programs &nbsp;|&nbsp; Voting Info &nbsp;|&nbsp; Contact &nbsp;|&nbsp; Donate</div>
  <div class="copyright">Copyright © 2019 Harmon Delia. &nbsp;All rights reserved.</div>
</footer>

</body>
</html>
```